Fun A1 2012 family planner using clever typography and block colour

I have been looking for an A1 2012 family planner and I have not been able to find one. Hence I would like help to develop such a planner. I plan to print it on matt paper, portrait orientated. I have attached some reference pictures of our 2011 planner. I like interesting typography, clear clean colours and simple illustration. I need space to write in daily events and need the weeks and days to be clearly delineated from each other. Each day cell needs the date and day in it (please refer to the file uploaded for a visual reference confirming this). Each weekend needs some kind of colour/ typographic delineation. I want a design for a year-at-a-view calendar. I plan to print the planner in Sydney, Australia with brightmarkprinthouse.com.au and probably to sell printed copies online. The terms & conditions of this project are that I will own the design concept 100% and in perpetuity worldwide once payment has been made. (NB. The attached Work File in Word contains a rough layout and all months, days and dates all typed up to make for quicker design.)

Target Market(s)

Reasonably well heeled family of 4. 2 parents. 2 kids. 2 pets.

Industry/Entity Type

Events

Requirements
Must have
• The calendar must be portrait (not landscape orientated), A1 size. It will be printed on matt paper by brightmarkprinthouse.com.au. It must have months running left to right (Jan-Dec) and day/date cells running top to bottom (refer 2011 planner photos in file uploaded). The day/ date cells must be around 3(w)x2(h)cm - big enough to write daily events in. Weekends must be colour/ typographically delineated. 2012 year must be noted as must "A Paperkite Inc Project" and web address in fine print bottom left hand left hand corner.
Nice to have
• A Paperkite Inc logo in bottom left hand corder (perhaps Merry Otter like: http://www.pixelvault-example.com/design_submission.aspx?designid=731604). Header/Footer space for customisation (e.g. "Brandt-Osei 2012 Planner" or "QRN Co 2012 Planner".
Should not have
• The calendar should not use photographs or resemble standard or cheesy wall calendars. No watermarks please.

```html
<!DOCTYPE html>
<html lang="en">
<head>
<meta charset="utf-8">
<title>Brandt-Osei 2012 Planner</title>
<link href="https://fonts.googleapis.com/css2?family=Didact+Gothic&family=Questrial&display=swap" rel="stylesheet">
<style>
:root{
  --stage:#d6d6d6;
  --paper:#f6e6c4;
  --teal:#2b8d9a;
  --teal-dark:#276a70;
  --leaf:#7e9a26;
  --weekday:#e6c79c;
  --ink:#3c3a38;
  --jan:#f26a22;
  --feb:#e8579b;
  --mar:#ef7d22;
  --apr:#e2164b;
  --may:#20bcc7;
  --jun:#2b9bb1;
  --jul:#24646c;
  --aug:#8ca11f;
  --sep:#6a7a1d;
  --oct:#6b2e13;
  --nov:#1f2a5b;
  --dec:#4a4645;
}
*{margin:0;padding:0;box-sizing:border-box}
html,body{width:1057px;height:1200px;overflow:hidden;background:var(--stage)}
.planner{position:absolute;left:128px;top:0;width:800px;height:1200px;background:var(--paper);font-family:"Didact Gothic",sans-serif}
.title{position:absolute;left:126px;top:58px;display:flex;align-items:baseline;gap:10px;color:var(--teal);font-family:"Questrial",sans-serif;font-size:31px;letter-spacing:.5px;white-space:nowrap;z-index:2}
.title .year{font-size:46px;color:var(--teal-dark);font-weight:400;letter-spacing:0}
.title .year em{font-style:normal;color:var(--leaf)}
.title-rule{position:absolute;left:668px;top:91px;width:132px;height:2px;background:var(--teal)}
.art{position:absolute;z-index:0}
.art-rabbit{left:52px;top:103px;width:24px;height:33px;background:#8a5a2e;border-radius:45% 45% 20% 20%}
.art-giraffe{left:440px;top:4px;width:58px;height:132px;background:linear-gradient(#9bb13a,#6f7d26);border-radius:40% 40% 8% 8%;opacity:.85}
.art-deer{left:664px;top:50px;width:34px;height:44px;background:var(--teal-dark);border-radius:30% 30% 10% 10%;opacity:.85}
.art-grove{left:612px;top:1147px;width:180px;height:38px;background:linear-gradient(90deg,#2f7b80,#2b8d9a);border-radius:50% 50% 6% 6%;opacity:.85}
.month{position:absolute;top:131px;width:56px;list-style:none;z-index:1}
.month-name{width:55px;height:55px;border-radius:50%;background:var(--m);color:#fff;display:flex;align-items:center;justify-content:center;font-family:"Questrial",sans-serif;font-size:23px;letter-spacing:-.5px;margin-bottom:10px;white-space:nowrap}
.days{list-style:none;display:flex;flex-direction:column;align-items:center;gap:2.6px}
.days li{width:28px;height:28px;border-radius:50%;background:var(--weekday);color:#fff;font-size:9.5px;line-height:1;display:flex;flex-direction:column;align-items:center;justify-content:center;padding-top:1px}
.days li small{font-size:5.5px;letter-spacing:.2px;margin-top:1px}
.days li.weekend{background:var(--m)}
.jan{left:38px;--m:var(--jan)}.feb{left:99.5px;--m:var(--feb)}.mar{left:161px;--m:var(--mar)}
.apr{left:222px;--m:var(--apr)}.may{left:283.5px;--m:var(--may)}.jun{left:345px;--m:var(--jun)}
.jul{left:406.5px;--m:var(--jul)}.aug{left:468px;--m:var(--aug)}.sep{left:529px;--m:var(--sep)}
.oct{left:590.5px;--m:var(--oct)}.nov{left:652px;--m:var(--nov)}.dec{left:713.5px;--m:var(--dec)}
.footer{position:absolute;left:15px;top:1179px;display:flex;align-items:center;font-size:10.5px;color:var(--ink);white-space:nowrap}
.footer .maker-mark{display:inline-block;width:14px;height:14px;border-radius:50%;background:var(--mar);margin:0 9px 0 12px}
.footer-rule{position:absolute;left:352px;top:1186px;width:444px;height:2px;background:var(--teal);z-index:0}
</style>
</head>
<body>
<main class="planner">
  <div class="art art-giraffe" role="img" aria-label="Green giraffe illustration reaching up through the year numerals"></div>
  <h1 class="title"><span>BRANDT-OSEI</span><span class="year">201<em>2</em></span><span>PLANNER</span></h1>
  <div class="title-rule"></div>
  <div class="art art-deer" role="img" aria-label="Small teal deer illustration standing on the title line"></div>
  <div class="art art-rabbit" role="img" aria-label="Brown rabbit illustration sitting on the January circle"></div>
  <div class="footer-rule"></div>
  <div class="art art-grove" role="img" aria-label="Teal silhouette of deer grazing beneath trees"></div>

  <section class="month jan"><h2 class="month-name">jan</h2><ol class="days">
<li class="weekend">1<small>SUN</small></li><li>2<small>MON</small></li><li>3<small>TUE</small></li><li>4<small>WED</small></li><li>5<small>THU</small></li><li>6<small>FRI</small></li><li class="weekend">7<small>SAT</small></li><li class="weekend">8<small>SUN</small></li><li>9<small>MON</small></li><li>10<small>TUE</small></li><li>11<small>WED</small></li><li>12<small>THU</small></li><li>13<small>FRI</small></li><li class="weekend">14<small>SAT</small></li><li class="weekend">15<small>SUN</small></li><li>16<small>MON</small></li><li>17<small>TUE</small></li><li>18<small>WED</small></li><li>19<small>THU</small></li><li>20<small>FRI</small></li><li class="weekend">21<small>SAT</small></li><li class="weekend">22<small>SUN</small></li><li>23<small>MON</small></li><li>24<small>TUE</small></li><li>25<small>WED</small></li><li>26<small>THU</small></li><li>27<small>FRI</small></li><li class="weekend">28<small>SAT</small></li><li class="weekend">29<small>SUN</small></li><li>30<small>MON</small></li><li>31<small>TUE</small></li>
  </ol></section>

  <section class="month feb"><h2 class="month-name">feb</h2><ol class="days">
<li>1<small>WED</small></li><li>2<small>THU</small></li><li>3<small>FRI</small></li><li class="weekend">4<small>SAT</small></li><li class="weekend">5<small>SUN</small></li><li>6<small>MON</small></li><li>7<small>TUE</small></li><li>8<small>WED</small></li><li>9<small>THU</small></li><li>10<small>FRI</small></li><li class="weekend">11<small>SAT</small></li><li class="weekend">12<small>SUN</small></li><li>13<small>MON</small></li><li>14<small>TUE</small></li><li>15<small>WED</small></li><li>16<small>THU</small></li><li>17<small>FRI</small></li><li class="weekend">18<small>SAT</small></li><li class="weekend">19<small>SUN</small></li><li>20<small>MON</small></li><li>21<small>TUE</small></li><li>22<small>WED</small></li><li>23<small>THU</small></li><li>24<small>FRI</small></li><li class="weekend">25<small>SAT</small></li><li class="weekend">26<small>SUN</small></li><li>27<small>MON</small></li><li>28<small>TUE</small></li><li>29<small>WED</small></li>
  </ol></section>

  <section class="month mar"><h2 class="month-name">mar</h2><ol class="days">
<li>1<small>THU</small></li><li>2<small>FRI</small></li><li class="weekend">3<small>SAT</small></li><li class="weekend">4<small>SUN</small></li><li>5<small>MON</small></li><li>6<small>TUE</small></li><li>7<small>WED</small></li><li>8<small>THU</small></li><li>9<small>FRI</small></li><li class="weekend">10<small>SAT</small></li><li class="weekend">11<small>SUN</small></li><li>12<small>MON</small></li><li>13<small>TUE</small></li><li>14<small>WED</small></li><li>15<small>THU</small></li><li>16<small>FRI</small></li><li class="weekend">17<small>SAT</small></li><li class="weekend">18<small>SUN</small></li><li>19<small>MON</small></li><li>20<small>TUE</small></li><li>21<small>WED</small></li><li>22<small>THU</small></li><li>23<small>FRI</small></li><li class="weekend">24<small>SAT</small></li><li class="weekend">25<small>SUN</small></li><li>26<small>MON</small></li><li>27<small>TUE</small></li><li>28<small>WED</small></li><li>29<small>THU</small></li><li>30<small>FRI</small></li><li class="weekend">31<small>SAT</small></li>
  </ol></section>

  <section class="month apr"><h2 class="month-name">apr</h2><ol class="days">
<li class="weekend">1<small>SUN</small></li><li>2<small>MON</small></li><li>3<small>TUE</small></li><li>4<small>WED</small></li><li>5<small>THU</small></li><li>6<small>FRI</small></li><li class="weekend">7<small>SAT</small></li><li class="weekend">8<small>SUN</small></li><li>9<small>MON</small></li><li>10<small>TUE</small></li><li>11<small>WED</small></li><li>12<small>THU</small></li><li>13<small>FRI</small></li><li class="weekend">14<small>SAT</small></li><li class="weekend">15<small>SUN</small></li><li>16<small>MON</small></li><li>17<small>TUE</small></li><li>18<small>WED</small></li><li>19<small>THU</small></li><li>20<small>FRI</small></li><li class="weekend">21<small>SAT</small></li><li class="weekend">22<small>SUN</small></li><li>23<small>MON</small></li><li>24<small>TUE</small></li><li>25<small>WED</small></li><li>26<small>THU</small></li><li>27<small>FRI</small></li><li class="weekend">28<small>SAT</small></li><li class="weekend">29<small>SUN</small></li><li>30<small>MON</small></li>
  </ol></section>

  <section class="month may"><h2 class="month-name">may</h2><ol class="days">
<li>1<small>TUE</small></li><li>2<small>WED</small></li><li>3<small>THU</small></li><li>4<small>FRI</small></li><li class="weekend">5<small>SAT</small></li><li class="weekend">6<small>SUN</small></li><li>7<small>MON</small></li><li>8<small>TUE</small></li><li>9<small>WED</small></li><li>10<small>THU</small></li><li>11<small>FRI</small></li><li class="weekend">12<small>SAT</small></li><li class="weekend">13<small>SUN</small></li><li>14<small>MON</small></li><li>15<small>TUE</small></li><li>16<small>WED</small></li><li>17<small>THU</small></li><li>18<small>FRI</small></li><li class="weekend">19<small>SAT</small></li><li class="weekend">20<small>SUN</small></li><li>21<small>MON</small></li><li>22<small>TUE</small></li><li>23<small>WED</small></li><li>24<small>THU</small></li><li>25<small>FRI</small></li><li class="weekend">26<small>SAT</small></li><li class="weekend">27<small>SUN</small></li><li>28<small>MON</small></li><li>29<small>TUE</small></li><li>30<small>WED</small></li><li>31<small>THU</small></li>
  </ol></section>

  <section class="month jun"><h2 class="month-name">jun</h2><ol class="days">
<li>1<small>FRI</small></li><li class="weekend">2<small>SAT</small></li><li class="weekend">3<small>SUN</small></li><li>4<small>MON</small></li><li>5<small>TUE</small></li><li>6<small>WED</small></li><li>7<small>THU</small></li><li>8<small>FRI</small></li><li class="weekend">9<small>SAT</small></li><li class="weekend">10<small>SUN</small></li><li>11<small>MON</small></li><li>12<small>TUE</small></li><li>13<small>WED</small></li><li>14<small>THU</small></li><li>15<small>FRI</small></li><li class="weekend">16<small>SAT</small></li><li class="weekend">17<small>SUN</small></li><li>18<small>MON</small></li><li>19<small>TUE</small></li><li>20<small>WED</small></li><li>21<small>THU</small></li><li>22<small>FRI</small></li><li class="weekend">23<small>SAT</small></li><li class="weekend">24<small>SUN</small></li><li>25<small>MON</small></li><li>26<small>TUE</small></li><li>27<small>WED</small></li><li>28<small>THU</small></li><li>29<small>FRI</small></li><li class="weekend">30<small>SAT</small></li>
  </ol></section>

  <section class="month jul"><h2 class="month-name">jul</h2><ol class="days">
<li class="weekend">1<small>SUN</small></li><li>2<small>MON</small></li><li>3<small>TUE</small></li><li>4<small>WED</small></li><li>5<small>THU</small></li><li>6<small>FRI</small></li><li class="weekend">7<small>SAT</small></li><li class="weekend">8<small>SUN</small></li><li>9<small>MON</small></li><li>10<small>TUE</small></li><li>11<small>WED</small></li><li>12<small>THU</small></li><li>13<small>FRI</small></li><li class="weekend">14<small>SAT</small></li><li class="weekend">15<small>SUN</small></li><li>16<small>MON</small></li><li>17<small>TUE</small></li><li>18<small>WED</small></li><li>19<small>THU</small></li><li>20<small>FRI</small></li><li class="weekend">21<small>SAT</small></li><li class="weekend">22<small>SUN</small></li><li>23<small>MON</small></li><li>24<small>TUE</small></li><li>25<small>WED</small></li><li>26<small>THU</small></li><li>27<small>FRI</small></li><li class="weekend">28<small>SAT</small></li><li class="weekend">29<small>SUN</small></li><li>30<small>MON</small></li><li>31<small>TUE</small></li>
  </ol></section>

  <section class="month aug"><h2 class="month-name">aug</h2><ol class="days">
<li>1<small>WED</small></li><li>2<small>THU</small></li><li>3<small>FRI</small></li><li class="weekend">4<small>SAT</small></li><li class="weekend">5<small>SUN</small></li><li>6<small>MON</small></li><li>7<small>TUE</small></li><li>8<small>WED</small></li><li>9<small>THU</small></li><li>10<small>FRI</small></li><li class="weekend">11<small>SAT</small></li><li class="weekend">12<small>SUN</small></li><li>13<small>MON</small></li><li>14<small>TUE</small></li><li>15<small>WED</small></li><li>16<small>THU</small></li><li>17<small>FRI</small></li><li class="weekend">18<small>SAT</small></li><li class="weekend">19<small>SUN</small></li><li>20<small>MON</small></li><li>21<small>TUE</small></li><li>22<small>WED</small></li><li>23<small>THU</small></li><li>24<small>FRI</small></li><li class="weekend">25<small>SAT</small></li><li class="weekend">26<small>SUN</small></li><li>27<small>MON</small></li><li>28<small>TUE</small></li><li>29<small>WED</small></li><li>30<small>THU</small></li><li>31<small>FRI</small></li>
  </ol></section>

  <section class="month sep"><h2 class="month-name">sep</h2><ol class="days">
<li class="weekend">1<small>SAT</small></li><li class="weekend">2<small>SUN</small></li><li>3<small>MON</small></li><li>4<small>TUE</small></li><li>5<small>WED</small></li><li>6<small>THU</small></li><li>7<small>FRI</small></li><li class="weekend">8<small>SAT</small></li><li class="weekend">9<small>SUN</small></li><li>10<small>MON</small></li><li>11<small>TUE</small></li><li>12<small>WED</small></li><li>13<small>THU</small></li><li>14<small>FRI</small></li><li class="weekend">15<small>SAT</small></li><li class="weekend">16<small>SUN</small></li><li>17<small>MON</small></li><li>18<small>TUE</small></li><li>19<small>WED</small></li><li>20<small>THU</small></li><li>21<small>FRI</small></li><li class="weekend">22<small>SAT</small></li><li class="weekend">23<small>SUN</small></li><li>24<small>MON</small></li><li>25<small>TUE</small></li><li>26<small>WED</small></li><li>27<small>THU</small></li><li>28<small>FRI</small></li><li class="weekend">29<small>SAT</small></li><li class="weekend">30<small>SUN</small></li>
  </ol></section>

  <section class="month oct"><h2 class="month-name">oct</h2><ol class="days">
<li>1<small>MON</small></li><li>2<small>TUE</small></li><li>3<small>WED</small></li><li>4<small>THU</small></li><li>5<small>FRI</small></li><li class="weekend">6<small>SAT</small></li><li class="weekend">7<small>SUN</small></li><li>8<small>MON</small></li><li>9<small>TUE</small></li><li>10<small>WED</small></li><li>11<small>THU</small></li><li>12<small>FRI</small></li><li class="weekend">13<small>SAT</small></li><li class="weekend">14<small>SUN</small></li><li>15<small>MON</small></li><li>16<small>TUE</small></li><li>17<small>WED</small></li><li>18<small>THU</small></li><li>19<small>FRI</small></li><li class="weekend">20<small>SAT</small></li><li class="weekend">21<small>SUN</small></li><li>22<small>MON</small></li><li>23<small>TUE</small></li><li>24<small>WED</small></li><li>25<small>THU</small></li><li>26<small>FRI</small></li><li class="weekend">27<small>SAT</small></li><li class="weekend">28<small>SUN</small></li><li>29<small>MON</small></li><li>30<small>TUE</small></li><li>31<small>WED</small></li>
  </ol></section>

  <section class="month nov"><h2 class="month-name">nov</h2><ol class="days">
<li>1<small>THU</small></li><li>2<small>FRI</small></li><li class="weekend">3<small>SAT</small></li><li class="weekend">4<small>SUN</small></li><li>5<small>MON</small></li><li>6<small>TUE</small></li><li>7<small>WED</small></li><li>8<small>THU</small></li><li>9<small>FRI</small></li><li class="weekend">10<small>SAT</small></li><li class="weekend">11<small>SUN</small></li><li>12<small>MON</small></li><li>13<small>TUE</small></li><li>14<small>WED</small></li><li>15<small>THU</small></li><li>16<small>FRI</small></li><li class="weekend">17<small>SAT</small></li><li class="weekend">18<small>SUN</small></li><li>19<small>MON</small></li><li>20<small>TUE</small></li><li>21<small>WED</small></li><li>22<small>THU</small></li><li>23<small>FRI</small></li><li class="weekend">24<small>SAT</small></li><li class="weekend">25<small>SUN</small></li><li>26<small>MON</small></li><li>27<small>TUE</small></li><li>28<small>WED</small></li><li>29<small>THU</small></li><li>30<small>FRI</small></li>
  </ol></section>

  <section class="month dec"><h2 class="month-name">dec</h2><ol class="days">
<li class="weekend">1<small>SAT</small></li><li class="weekend">2<small>SUN</small></li><li>3<small>MON</small></li><li>4<small>TUE</small></li><li>5<small>WED</small></li><li>6<small>THU</small></li><li>7<small>FRI</small></li><li class="weekend">8<small>SAT</small></li><li class="weekend">9<small>SUN</small></li><li>10<small>MON</small></li><li>11<small>TUE</small></li><li>12<small>WED</small></li><li>13<small>THU</small></li><li>14<small>FRI</small></li><li class="weekend">15<small>SAT</small></li><li class="weekend">16<small>SUN</small></li><li>17<small>MON</small></li><li>18<small>TUE</small></li><li>19<small>WED</small></li><li>20<small>THU</small></li><li>21<small>FRI</small></li><li class="weekend">22<small>SAT</small></li><li class="weekend">23<small>SUN</small></li><li>24<small>MON</small></li><li>25<small>TUE</small></li><li>26<small>WED</small></li><li>27<small>THU</small></li><li>28<small>FRI</small></li><li class="weekend">29<small>SAT</small></li><li class="weekend">30<small>SUN</small></li><li>31<small>MON</small></li>
  </ol></section>

  <footer class="footer"><span>A Paperkite Inc Project</span><span class="maker-mark"></span><span>brightmarkprinthouse.com.au</span></footer>
</main>
</body>
</html>
```